Our swimming pool service needs your help with letterhead

Letterhead for small swimming pool service- We would like a professional look with a creative layout- must be compatible with LedgerNest forms (sample attached)
No more than 2 colors in graphics

Target Market(s)

Homeowners/ Contractors

Font styles to use
Sans Serif

Colors
33a6d7
85cae6

Requirements
Must have
• Logo (file attached)
• Compatible with LedgerNest (sample attached)
• Mailing address- P.O. Box 58, Cedar Hollow NY 11592
• phone- (631) 529-6180
• email- marcdoylewater@mailbrook.net
• Licensed & Insured
Nice to have
• Small slogan- Examples:Family owned and operated for 25 years, 25 years of trusted service
• Creative layout
Should not have
• Blue color must be same as blue in our logo
• No thick lines of color
• No design in middle of page

```html
<!DOCTYPE html>
<html lang="en">
<head>
<meta charset="utf-8">
<title>Marc D. Doyle Pool Service – Invoice</title>
<link rel="stylesheet" href="https://fonts.googleapis.com/css2?family=Poppins:wght@400;500;600&family=Roboto+Condensed:wght@400&display=swap">
<style>
  :root {
    --navy: #243a5e;
    --ink: #2b3f66;
    --sky: #6aafe0;
    --brand-blue: #33a6d7;
    --rule: #c9c9c9;
    --text: #222;
    --muted: #444;
    --paper: #ffffff;
  }
  * { margin: 0; padding: 0; box-sizing: border-box; }
  html, body { width: 937px; height: 1200px; overflow: hidden; background: var(--paper); }
  body { font-family: "Poppins", sans-serif; color: var(--text); position: relative; }

  .brand {
    position: absolute; top: 52px; left: 0; width: 937px;
    display: flex; justify-content: center; align-items: center; gap: 14px;
  }
  .brand-dot { width: 40px; height: 40px; border-radius: 50%; background: var(--brand-blue); }
  .brand-name { font-size: 34px; font-weight: 600; color: var(--navy); letter-spacing: 1px; line-height: 1; }

  .bill-to { position: absolute; left: 58px; top: 194px; color: var(--ink); font-size: 15px; letter-spacing: 0.8px; line-height: 24px; }
  .bill-to .label { margin-bottom: 4px; }

  .invoice-meta {
    position: absolute; left: 687px; top: 176px; height: 90px;
    border-left: 1px solid var(--rule); padding-left: 14px;
    color: var(--ink); font-size: 15px; line-height: 27.5px; padding-top: 16px;
  }

  .items { position: absolute; left: 32px; top: 325px; width: 873px; }
  .items-head {
    height: 35px; background: var(--navy); color: #fff; font-size: 13.5px; font-weight: 500;
    display: grid; grid-template-columns: 366px 166px 186px 155px; align-items: center;
  }
  .items-head span:first-child { padding-left: 21px; }
  .items-head span:not(:first-child) { text-align: center; }
  .items-body {
    height: 505px; border: 1px solid var(--rule); border-top: none;
    display: grid; grid-template-columns: 366px 166px 186px 155px; font-size: 16.5px;
  }
  .col + .col { border-left: 1px solid var(--rule); }
  .col-desc { padding: 4px 0 0 21px; line-height: 44px; }
  .col-rate, .col-amount { padding-top: 16px; line-height: 36px; text-align: center; }

  .payment { position: absolute; left: 35px; top: 876px; color: var(--ink); font-size: 14.5px; }
  .payment p { line-height: 26px; }
  .contact { list-style: none; margin-top: 8px; color: var(--muted); font-size: 14.5px; }
  .contact li { display: flex; align-items: center; gap: 14px; height: 31px; }
  .contact svg { width: 16px; height: 16px; fill: var(--navy); flex: none; }

  .totals { position: absolute; left: 564px; top: 865px; width: 341px; border-left: 1px solid var(--rule); border-right: 1px solid var(--rule); border-bottom: 1px solid var(--rule); }
  .totals-row { display: grid; grid-template-columns: 186px 155px; border-top: 1px solid var(--rule); height: 44px; align-items: center; }
  .totals-row:first-child { border-top: none; }
  .totals-row .name { font-family: "Roboto Condensed", sans-serif; font-size: 15px; padding-left: 8px; color: #333; }
  .totals-row .value { text-align: center; font-size: 15.5px; border-left: 1px solid var(--rule); height: 100%; display: flex; align-items: center; justify-content: center; }

  .footer-accent { position: absolute; left: 0; top: 1114px; width: 937px; height: 3px; background: var(--sky); }
  .footer-band {
    position: absolute; left: 0; top: 1124px; width: 937px; height: 76px; background: var(--navy);
  }
  .footer-text { position: absolute; right: 46px; top: 1137px; color: #fff; font-size: 18px; font-weight: 500; text-align: center; line-height: 25px; }
</style>
</head>
<body>
  <header class="brand">
    <div class="brand-dot"></div>
    <div class="brand-name">MARC D. DOYLE POOL SERVICE</div>
  </header>

  <section class="bill-to">
    <p class="label">BILL TO</p>
    <p>Sample, 123 Avenue</p>
    <p>Anywhere, USA</p>
  </section>

  <section class="invoice-meta">
    <p>Date: 9/11/2019</p>
    <p>Invoice No. 11676</p>
    <p>Terms:&nbsp; Due On Receipt</p>
  </section>

  <section class="items">
    <div class="items-head">
      <span>Description</span><span>Quantity</span><span>Rate</span><span>Amount</span>
    </div>
    <div class="items-body">
      <div class="col col-desc"><p>Labor</p><p>Sales Tax</p></div>
      <div class="col col-qty"></div>
      <div class="col col-rate"><p>0.00</p><p>8.625 %</p></div>
      <div class="col col-amount"><p>0.00</p><p>0.00</p></div>
    </div>
  </section>

  <section class="payment">
    <p>Check Payable To Marc D. Doyle.</p>
    <p>Charge By Phone.</p>
    <ul class="contact">
      <li><svg viewBox="0 0 16 16"><path d="M4 1h8v14H4z M5.5 3v4h5V3z M5.5 9h1.5v1.3H5.5z M7.3 9h1.5v1.3H7.3z M9 9h1.5v1.3H9z M5.5 11h1.5v1.3H5.5z M7.3 11h1.5v1.3H7.3z M9 11h1.5v1.3H9z" fill-rule="evenodd"/></svg>(631) 529-6180</li>
      <li><svg viewBox="0 0 16 16"><path d="M0 3h16v1.2L8 9 0 4.2z M0 5.6l8 4.8 8-4.8V13H0z"/></svg>marcdoylewater@mailbrook.net</li>
      <li><svg viewBox="0 0 16 16"><path d="M8 0a5.5 5.5 0 0 0-5.5 5.5C2.5 10 8 16 8 16s5.5-6 5.5-10.5A5.5 5.5 0 0 0 8 0zm0 8a2.4 2.4 0 1 1 0-4.8A2.4 2.4 0 0 1 8 8z"/></svg>P.O. Box 58, Cedar Hollow NY 11592</li>
    </ul>
  </section>

  <section class="totals">
    <div class="totals-row"><span class="name">Subtotal</span><span class="value">0.00</span></div>
    <div class="totals-row"><span class="name">Rounding Off Amt.</span><span class="value">0.00</span></div>
    <div class="totals-row"><span class="name">Invoice Currency USD $</span><span class="value">0.00</span></div>
  </section>

  <div class="footer-accent"></div>
  <footer class="footer-band"></footer>
  <div class="footer-text">
    <p>Licensed &amp; Insured</p>
    <p>Family Owned And Operated For 25 Years</p>
  </div>
</body>
</html>
```